Granite Civic Builders Summit (GCBS) needs a flyer and logo design

We need a save the date flyer that can be easily edited to be a header only with event title, date and location.
We also are looking for a conference logo that will go well with our company logo.
Updates
Most of you are submitting an agenda design. Not a graphic flyer design. This isn't what I'm needing. I need something that can easily be a save the date with a header and is graphically appealing. Additionally, I've only gotten 2 logo designs.
Low design quality
Target Market(s)
Architects, engineers, public owners, contractors, attorneys
Industry/Entity Type
Construction
Logo Text
Granite Civic Builder's Summit
Requirements
Must have
- Flyer should Have:
- Title: "A Lantern Across Stormy Seas - Project Delivery to Operations”
- Date: August 8-9, 2019
- Location: Fort Worth, TX
- One-page only
- Conference Logo should be relatable to our company logo: Granite Civic Builders Summit.
Nice to have
- Topics:
- Alternative Constrcting: JOC & Design-Build
- Dealing with Contracting in a Tight TX Industry
- Tools & Technologies Project Delivery and Operations: Design and Construction
- Tools & Technologies: Coordinating Operations
Should not have
- Detailed agenda

```html
<!DOCTYPE html>
<html lang="en">
<head>
<meta charset="utf-8">
<title>A Lantern Across Stormy Seas – Save the Date</title>
<link rel="stylesheet" href="https://fonts.googleapis.com/css2?family=Oswald:wght@600;700&family=Open+Sans:wght@400;600;700&display=swap">
<style>
  :root {
    --green: #8fb43d;
    --green-dark: #6f9a2a;
    --blue: #0b5fa8;
    --blue-deep: #0a3a8a;
    --blue-line: #1b6fb5;
    --card: #e7e8ea;
    --ink: #3a3a3a;
    --white: #ffffff;
    --rule: #c9d9a8;
  }
  * { box-sizing: border-box; margin: 0; padding: 0; }
  html, body { width: 961px; height: 1200px; overflow: hidden; background: var(--white); }
  .flyer { width: 961px; height: 1200px; display: flex; flex-direction: column; font-family: "Open Sans", sans-serif; }

  .header { height: 239px; background: var(--green); text-align: center; color: var(--white); padding-top: 44px; }
  .event-title { font-family: "Oswald", sans-serif; font-weight: 700; font-size: 52px; line-height: 1; letter-spacing: 0.5px; text-shadow: 1px 2px 3px rgba(0,0,0,.3); }
  .event-subtitle { font-weight: 700; font-size: 31px; margin-top: 16px; text-shadow: 1px 2px 3px rgba(0,0,0,.25); }
  .header-rule { width: 590px; height: 2px; background: var(--rule); margin: 20px auto 0; }
  .event-meta { margin-top: 16px; font-size: 18px; font-weight: 600; }
  .event-meta strong { font-size: 23px; font-weight: 600; }
  .event-meta .gap { display: inline-block; width: 30px; }

  .band-line { height: 6px; background: linear-gradient(90deg, var(--blue-line), var(--blue-deep)); }

  .hero { height: 482px; background:
      linear-gradient(180deg, #d9dcdf 0%, #f4f3ef 40%, #fbf6ea 55%, #bfbcb6 70%, #55565a 100%); }

  .topics { height: 327px; background: linear-gradient(180deg, var(--blue) 0%, var(--blue-deep) 100%); position: relative; }
  .topics-heading { font-family: "Oswald", sans-serif; font-weight: 700; font-size: 66px; color: var(--white); text-align: center; letter-spacing: 26px; padding-left: 26px; line-height: 1; padding-top: 22px; text-shadow: 2px 3px 4px rgba(0,0,0,.35); }
  .topic-list { position: absolute; left: 48px; top: 102px; display: flex; gap: 9px; list-style: none; }
  .topic-card { height: 205px; background: var(--card); border-radius: 8px; color: var(--ink); font-weight: 700; font-size: 20.5px; line-height: 1.33; text-align: center; padding: 12px 8px 0; box-shadow: 0 2px 4px rgba(0,0,0,.25); }
  .topic-card .detail { display: block; margin-top: 9px; }
  .w1 { width: 183px; } .w2 { width: 176px; } .w3 { width: 263px; } .w4 { width: 210px; }

  .footer { height: 146px; background: var(--white); display: flex; align-items: center; justify-content: space-between; padding: 0 52px 0 56px; box-shadow: inset 0 14px 14px -12px rgba(0,0,0,.35); }
  .brand { display: flex; align-items: center; gap: 16px; }
  .brand-dot { width: 56px; height: 56px; border-radius: 50%; }
  .brand-institute .brand-dot { background: var(--blue-deep); }
  .brand-institute .brand-name { font-size: 22px; font-weight: 600; color: var(--blue-deep); }
  .brand-summit .brand-dot { background: var(--green); }
  .brand-summit .brand-name { font-size: 21px; font-weight: 400; color: #222; line-height: 1.2; text-transform: uppercase; }
</style>
</head>
<body>
<main class="flyer">
  <header class="header">
    <h1 class="event-title">A LANTERN ACROSS STORMY SEAS</h1>
    <p class="event-subtitle">Project Delivery to Operations</p>
    <div class="header-rule"></div>
    <p class="event-meta">Date: <strong>August 8-9, 2019</strong><span class="gap"></span>Location: <strong>Fort Worth, TX</strong></p>
  </header>
  <div class="band-line"></div>
  <div class="hero" role="img" aria-label="Photo of a hand drawing a long bridge road with a pencil, stretching into a bright hazy sky"></div>
  <section class="topics">
    <h2 class="topics-heading">TOPICS</h2>
    <ul class="topic-list">
      <li class="topic-card w1">Alternative Constrcting:<span class="detail">JOC &amp;<br>Design-<br>Build</span></li>
      <li class="topic-card w2">Dealing<br>with<br>Contracting<br>in a Tight<br>TX<br>Industry</li>
      <li class="topic-card w3">Tools &amp;<br>Technologies<br>Project Delivery<br>and Operations:<span class="detail">Design and<br>Construction</span></li>
      <li class="topic-card w4">Tools &amp;<br>Technologies:<span class="detail">Coordinating<br>Operations</span></li>
    </ul>
  </section>
  <footer class="footer">
    <div class="brand brand-institute">
      <span class="brand-dot"></span>
      <span class="brand-name">Capital Stewards Institute</span>
    </div>
    <div class="brand brand-summit">
      <span class="brand-dot"></span>
      <span class="brand-name">Granite Civic<br>Builders Summit</span>
    </div>
  </footer>
</main>
</body>
</html>
```